Overview of Elder Abuse Resources Brochure

We need a 2-page brochure that provides a list of resources for elders in tribal communities in the US and those who care for them. We want it to be simple and easy to read, and easy to see the difference between each resource. We would also like eye-catching images or graphics. Please keep the images on the front, and add any photos or graphics that depict Native American elders. We need both of our logos on the first page, in the far-right column. Please refer to the attached image for our brand colors and a font suggestion. Please keep the three columns on each page, but delete the blank pages in the document.

```html
<!DOCTYPE html>
<html lang="en">
<head>
<meta charset="utf-8">
<title>Services for Elders &amp; People Who Care for Them</title>
<link href="https://fonts.googleapis.com/css2?family=Barlow:wght@400;500&family=Barlow+Semi+Condensed:wght@500;600;700&family=Rubik:wght@600;700&display=swap" rel="stylesheet">
<style>
:root{
  --teal:#1f6e78;
  --teal-light:#4fa9b3;
  --cyan:#2cc4d4;
  --red:#b05a50;
  --maroon:#3a1416;
  --ink:#141414;
  --grey:#9a9a9a;
  --paper:#ffffff;
  --navy:#0b2530;
  --gold:#c9a45a;
}
*{box-sizing:border-box;margin:0;padding:0}
html,body{width:1200px;height:848px;overflow:hidden;background:var(--paper)}
body{font-family:"Barlow",sans-serif;color:var(--ink);position:relative}
.panel{position:absolute;top:0;height:832px}
.panel--inside{left:0;width:400px}
.panel--mailer{left:400px;width:401px;background:var(--teal)}
.panel--cover{left:801px;width:399px}
.base-band{position:absolute;left:0;bottom:0;width:1200px;height:16px;
  background:linear-gradient(90deg,#cfe3e6,#e8c9c4,#cfe3e6)}

/* left panel */
.section-title{position:absolute;left:39px;top:32px;font-family:"Barlow Semi Condensed",sans-serif;font-weight:700;font-size:35px;color:var(--teal);letter-spacing:.2px}
.section-title span{color:var(--red)}
.intro{position:absolute;left:39px;top:93px;width:330px;font-size:16.4px;line-height:20.5px}
.intro p{margin-bottom:21px}
.help-box{position:absolute;left:39px;top:349px;width:324px}
.help-box__head{background:var(--red);color:#fff;font-family:"Rubik",sans-serif;font-weight:700;font-size:22px;text-align:center;height:36px;line-height:36px}
.help-box__sub{background:var(--teal);color:#fff;font-size:16.4px;line-height:20.5px;text-align:center;padding:8px 10px;height:58px}
.help-box__fill{border:1px solid #b8b8b8;height:104px;color:var(--grey);font-size:16.4px;line-height:20.5px;text-align:center;padding:20px 40px 0}
.resource{position:absolute;left:39px;width:326px;text-align:center;font-size:16.4px;line-height:20.5px}
.resource--locator{top:570px}
.resource--locator .num{font-family:"Rubik",sans-serif;font-weight:700;font-size:20px;color:var(--teal);display:block;margin-top:3px}
.rule{position:absolute;left:39px;width:326px;height:1px;background:#cfcfcf}
.resource--emergency{top:657px;font-family:"Rubik",sans-serif;font-weight:700;font-size:20px}
.resource--emergency em{font-style:normal;color:var(--red)}
.resource--mental{top:703px}
.resource--mental b{font-family:"Rubik",sans-serif;font-weight:700;color:var(--red)}
.resource--safety{top:764px}
.resource--safety .num{font-family:"Rubik",sans-serif;font-weight:700;font-size:20px;color:var(--teal);display:block;margin-top:2px}

/* mailer panel */
.vertical{position:absolute;writing-mode:vertical-rl;transform:rotate(180deg);color:#fff;white-space:nowrap}
.org-name{left:330px;top:45px;height:190px;font-family:"Barlow Semi Condensed",sans-serif;font-weight:700;font-size:16px;line-height:17px;text-transform:uppercase}
.address{font-size:16.5px;line-height:20.5px}
.address b{font-family:"Rubik",sans-serif;font-weight:700}
.address--recipient{left:48px;top:420px;height:152px}
.address--sender{left:48px;top:640px;height:145px}
.contact--web{left:325px;top:480px;height:92px;font-size:16.5px;line-height:20.5px}
.contact--phone{left:325px;top:690px;height:95px;font-size:16.5px;line-height:20.5px}

/* cover panel */
.brand{position:absolute;left:33px;top:40px;display:flex;align-items:center;gap:12px}
.brand__mark{width:40px;height:40px;background:var(--teal-light)}
.brand__name{font-family:"Barlow Semi Condensed",sans-serif;font-weight:700;font-size:24px;line-height:24px;color:var(--red);width:300px}
.pattern{position:absolute;left:0;width:399px;height:20px}
.pattern--top{top:125px;background:linear-gradient(90deg,#f4e4e1,var(--red))}
.pattern--mid{top:388px;background:linear-gradient(90deg,var(--teal-light),#e3f1f3)}
.hero{position:absolute;left:0;top:147px;width:399px;height:238px;background:var(--maroon);text-align:center;color:#fff}
.hero__kicker{font-family:"Barlow Semi Condensed",sans-serif;font-weight:700;font-size:38px;color:var(--cyan);margin-top:35px;line-height:42px}
.hero__title{font-family:"Barlow Semi Condensed",sans-serif;font-weight:700;font-size:40px;line-height:45px}
.hero__rule{width:328px;height:1px;background:var(--red);margin:10px auto 0}
.hero__who{font-family:"Barlow Semi Condensed",sans-serif;font-weight:500;font-size:13.5px;color:var(--red);margin-top:10px}
.photo{position:absolute;left:0;top:410px;width:399px;height:228px;
  background:linear-gradient(180deg,#3f6fae 0%,#7aa2cf 35%,#b0694a 70%,#7a3a28 100%)}
.prompts{position:absolute;left:20px;top:660px;width:220px}
.prompt{display:flex;align-items:center;gap:12px;height:50px}
.prompt+.prompt{border-top:1px solid #d5d5d5}
.prompt:nth-child(1){height:46px}
.prompt:nth-child(3){height:60px}
.prompt__icon{flex:none;width:37px;height:37px;border-radius:50%;background:var(--red);display:flex;align-items:center;justify-content:center}
.prompt__text{font-family:"Barlow Semi Condensed",sans-serif;font-weight:500;font-size:13.5px;line-height:16.5px}
.partner-badge{position:absolute;left:241px;top:668px;width:132px;height:141px;background:var(--navy);border:2px solid var(--navy);outline:1px solid var(--gold);outline-offset:-6px}
</style>
</head>
<body>

<section class="panel panel--inside">
  <h2 class="section-title">RESPECT FOR <span>ELDERS</span></h2>
  <div class="intro">
    <p>Do you have concerns about an Elder, maybe you see that they are not taking care of themselves, or family only comes once a month when the Elder has money?</p>
    <p>Is an Elder telling you that they are not treated with respect or that someone is bothering them?</p>
    <p>These may be signs of Elder abuse, neglect or exploitation.</p>
  </div>
  <div class="help-box">
    <div class="help-box__head">FOR HELP CONTACT</div>
    <div class="help-box__sub">Your Tribal Social Services or Elders Department:</div>
    <div class="help-box__fill">Insert contact information for your tribal services, law enforcement, etc.</div>
  </div>
  <p class="resource resource--locator">The Elder Care Finder for information on Adult Protective Services <span class="num">1-800-555-0142</span></p>
  <div class="rule" style="top:646px"></div>
  <p class="resource resource--emergency">If a serious emergency, <em>call 911.</em></p>
  <div class="rule" style="top:694px"></div>
  <p class="resource resource--mental">For mental health support for yourself or an Elder, <b>call or text 555-0188</b></p>
  <div class="rule" style="top:755px"></div>
  <p class="resource resource--safety">Family Safety Line <span class="num">1.800.555.0199</span></p>
</section>

<section class="panel panel--mailer">
  <div class="vertical org-name">Council for<br>Native Elder Wellbeing</div>
  <div class="vertical address address--recipient"><b>Recipient</b><br>Street Address<br>City, ST ZIP Code</div>
  <div class="vertical address address--sender"><b>Company Name</b><br>Street Address<br>City, ST ZIP</div>
  <div class="vertical contact--web">Website<br>Email</div>
  <div class="vertical contact--phone">Telephone<br>Fax</div>
</section>

<section class="panel panel--cover">
  <div class="brand">
    <span class="brand__mark"></span>
    <span class="brand__name">Council for Native Elder Wellbeing</span>
  </div>
  <div class="pattern pattern--top" role="img" aria-label="Woven zigzag border pattern in rose tones"></div>
  <div class="hero">
    <p class="hero__kicker">Services for</p>
    <h1 class="hero__title">Elders &amp; People<br>Who Care for Them</h1>
    <div class="hero__rule"></div>
    <p class="hero__who">My Mother | My Father | My Sister &nbsp;| My Grandchild &nbsp;| Myself</p>
  </div>
  <div class="pattern pattern--mid" role="img" aria-label="Woven zigzag border pattern in teal tones"></div>
  <div class="photo" role="img" aria-label="Photo of a Native American grandmother holding a woven basket beside a young granddaughter, desert mesas under a blue sky"></div>
  <div class="prompts">
    <div class="prompt">
      <span class="prompt__icon"><svg width="20" height="22" viewBox="0 0 20 22" aria-hidden="true"><circle cx="10" cy="6" r="4.5" fill="#fff"/><path d="M2 21c0-5 3.5-8 8-8s8 3 8 8z" fill="#fff"/></svg></span>
      <span class="prompt__text">Are you caring for an Elder or a Grandchild?</span>
    </div>
    <div class="prompt">
      <span class="prompt__icon"><svg width="20" height="22" viewBox="0 0 20 22" aria-hidden="true"><circle cx="10" cy="6" r="4.5" fill="#fff"/><path d="M2 21c0-5 3.5-8 8-8s8 3 8 8z" fill="#fff"/></svg></span>
      <span class="prompt__text">Are you an Elder who needs help staying at home?</span>
    </div>
    <div class="prompt">
      <span class="prompt__icon"><svg width="20" height="22" viewBox="0 0 20 22" aria-hidden="true"><circle cx="10" cy="6" r="4.5" fill="#fff"/><path d="M2 21c0-5 3.5-8 8-8s8 3 8 8z" fill="#fff"/></svg></span>
      <span class="prompt__text">These programs and information can be a helpful resource.</span>
    </div>
  </div>
  <div class="partner-badge" role="img" aria-label="Partner organization badge"></div>
</section>

<div class="base-band" role="img" aria-label="Woven zigzag border pattern in teal and rose"></div>

</body>
</html>
```